Dental Trade Show Brochure

We need a brochure that is created for dental professionals that will explain how our Compliance Management Platform can help them to simplify, centralize and automate their compliance and other documentation requirements for their practices.

would like the content to be refreshed for dental practices. “EHS” should go away, as healthcare has many compliance requirements, not just health and safety. You are the experts. I am looking for your creative genius to help guide me to the right brochure that has text, imagery and design that will speak to my audience.

Target Market(s)

Dental Industry

Industry/Entity Type

Dental

Requirements
Must have
• would like the content to be refreshed for dental practices. “EHS” should go away, as healthcare has many compliance requirements, not just health and safety. You are the experts. I am looking for your creative genius to help guide me to the right brochure that has text, imagery and design that will speak to my audience.
Nice to have
• We prefer 1 front/back page over bi or tri fold
Should not have
• Other Industry graphics, design, content.

```html
<!DOCTYPE html>
<html lang="en">
<head>
<meta charset="UTF-8">
<title>Vantrix Comply Dental Brochure Cover</title>
<link href="https://fonts.googleapis.com/css2?family=Poppins:wght@500;600;800&display=swap" rel="stylesheet">
<style>
  :root {
    --stage: #e9e9ec;
    --paper: #f4f5f7;
    --navy: #14187a;
    --royal: #1c2bd6;
    --indigo: #2a2f9e;
    --sky: #4d8ef5;
    --pale-blue: #b9cdfa;
    --ice: #dbe6fd;
    --white: #ffffff;
  }
  * { box-sizing: border-box; margin: 0; padding: 0; }
  html, body {
    width: 1200px; height: 1200px; overflow: hidden;
    background: var(--stage);
    font-family: "Poppins", sans-serif;
  }
  .stage {
    width: 1200px; height: 1200px;
    display: flex; align-items: center; justify-content: center;
  }
  .cover {
    position: relative;
    width: 780px; height: 1100px;
    background: var(--paper);
    overflow: hidden;
    box-shadow: 0 12px 40px rgba(20, 24, 60, 0.18);
  }
  .brand {
    position: absolute; top: 72px; right: 64px;
    display: flex; align-items: center; gap: 12px;
  }
  .brand-mark {
    width: 30px; height: 30px; background: var(--royal); border-radius: 4px;
  }
  .brand-name {
    font-weight: 600; font-size: 34px; color: var(--royal); letter-spacing: -0.5px;
  }
  .blue-panel {
    position: absolute; left: 0; right: 0; top: 560px; bottom: 0;
    background: linear-gradient(135deg, var(--navy) 0%, var(--indigo) 55%, #3036b4 100%);
  }
  .blue-panel::before {
    content: ""; position: absolute; left: 0; right: 0; top: 0; height: 26px;
    background: var(--royal);
  }
  .blue-panel::after {
    content: ""; position: absolute; left: 0; right: 0; bottom: 0; height: 120px;
    background: linear-gradient(90deg, var(--royal), #2f3ce0);
  }
  .dot-grid {
    position: absolute; right: 60px; top: 680px; width: 200px; height: 56px;
    background-image: radial-gradient(circle, rgba(120,150,255,0.55) 1.4px, transparent 1.6px);
    background-size: 22px 22px;
  }
  .photo-frame {
    position: absolute; left: 210px; top: 160px; width: 560px; height: 500px;
  }
  .headline {
    position: absolute; left: 56px; top: 760px;
    font-weight: 800; font-size: 50px; line-height: 1.12; letter-spacing: 0.5px;
  }
  .headline .lead { color: var(--white); display: block; }
  .headline .rest { color: var(--pale-blue); display: block; }
  .web-address {
    position: absolute; left: 56px; bottom: 42px;
    font-weight: 600; font-size: 24px; color: var(--ice); z-index: 2;
  }
</style>
</head>
<body>
<main class="stage">
  <article class="cover">
    <div class="brand">
      <span class="brand-mark"></span>
      <span class="brand-name">Vantrix Comply</span>
    </div>

    <div class="blue-panel"></div>
    <div class="dot-grid"></div>

    <svg class="photo-frame" viewBox="0 0 560 500">
      <defs>
        <linearGradient id="frameGradient" x1="0" y1="0" x2="1" y2="1">
          <stop offset="0" stop-color="#cfdcfb"/>
          <stop offset="1" stop-color="#3f7ef0"/>
        </linearGradient>
        <linearGradient id="photoTone" x1="0" y1="0" x2="1" y2="1">
          <stop offset="0" stop-color="#c9d6e6"/>
          <stop offset="0.45" stop-color="#5b9be0"/>
          <stop offset="0.75" stop-color="#e6ecf3"/>
          <stop offset="1" stop-color="#8aa6c4"/>
        </linearGradient>
      </defs>
      <polygon class="hex-frame" points="140,10 420,10 550,250 420,490 140,490 10,250" fill="url(#frameGradient)"/>
      <polygon class="hex-photo" role="img"
        aria-label="Photo: a dentist and practice manager reviewing compliance records on a tablet in a modern dental clinic"
        points="152,30 408,30 528,250 408,470 152,470 32,250" fill="url(#photoTone)"/>
    </svg>

    <h1 class="headline">
      <span class="lead">Simplify Your Dental</span>
      <span class="rest">Practice Compliance</span>
      <span class="rest">with the Right Tools</span>
    </h1>

    <p class="web-address">www.vantrixhq.cloud</p>
  </article>
</main>
</body>
</html>
```